card design for engineering consultancy

engineering drafting and project management company the provides drafting services for.
Electrical, Hydraulic, Mechanical, and Civil services
The company is called Q7R Services and logo is as attached
Information on card should be.
1. Logo
2.website : Q7RServices.example
3. email : info@Q7RServices.example
4. Phone: (+61) 400512836
5. Motto: Design - Document - Develop - Deliver

this card should be basically used for business identification only

Target Market(s)

electricians plumbers air conditioning installers and civil contractors

Industry/Entity Type

engineering, drafting, electrical, plumbing, airconditioning, civil

Contact Information for Business Card

1. Logo 2.website : Q7RServices.example 3. email : info@Q7RServices.example 4. Phone: (+61) 400512836 5. Motto: Design - Document - Develop - Deliver

Font styles to use
Serif

Requirements
Must have
• logo
Nice to have
• something inovative and different that makes it stand out from being just another business card

```html
<!DOCTYPE html>
<html lang="en">
<head>
<meta charset="utf-8">
<title>Q7R Services – Business Card</title>
<link href="https://fonts.googleapis.com/css2?family=Montserrat:wght@400;500;700;800&display=swap" rel="stylesheet">
<style>
  :root{
    --bg:#ecebe8;
    --charcoal:#444546;
    --red:#c8202b;
    --white:#ffffff;
    --paper:#f7f7f7;
    --ink:#3d3d3d;
    --silver-hi:#f1f1f1;
    --silver-lo:#b9b9b9;
  }
  *{margin:0;padding:0;box-sizing:border-box}
  html,body{width:1157px;height:1200px;overflow:hidden;background:var(--bg);
    font-family:"Montserrat",sans-serif}
  .sheet{position:relative;width:1157px;height:1200px}
  .card{position:absolute;left:138px;width:880px;height:503px;overflow:hidden;
    box-shadow:0 6px 18px rgba(0,0,0,.18)}
  .card--back{top:56px;
    background:linear-gradient(125deg,var(--silver-lo) 0%,var(--silver-hi) 45%,#d2d2d2 70%,var(--silver-lo) 100%)}
  .back-brand{position:absolute;inset:0;display:flex;align-items:center;justify-content:center;gap:16px}
  .back-brand__mark{width:26px;height:26px;background:var(--charcoal)}
  .back-brand__name{font-size:40px;font-weight:800;letter-spacing:3px;color:var(--charcoal);text-transform:uppercase}

  .card--front{top:641px;background:var(--charcoal)}
  .card__art{position:absolute;inset:0}
  .contact{position:absolute;left:96px;top:56px}
  .contact__title{font-size:31px;font-weight:800;color:var(--red);text-transform:uppercase;letter-spacing:.5px}
  .contact__rule{width:74px;height:4px;background:var(--red);margin:12px 0 14px}
  .contact__motto{font-size:16px;font-weight:500;color:var(--ink);line-height:1.35;letter-spacing:.5px}
  .contact__list{list-style:none;margin-top:20px}
  .contact__item{display:flex;align-items:center;gap:20px;height:44px;font-size:17px;font-weight:500;
    color:var(--ink);letter-spacing:.6px}
  .icon{width:32px;height:32px;border-radius:50%;background:var(--red);display:flex;
    align-items:center;justify-content:center;flex:none}
  .divider{position:absolute;left:450px;top:78px;width:4px;height:300px;background:var(--charcoal)}
  .front-brand{position:absolute;left:454px;right:24px;top:0;height:420px;display:flex;
    align-items:center;justify-content:center;gap:14px}
  .front-brand__mark{width:24px;height:24px;background:var(--charcoal)}
  .front-brand__name{font-size:36px;font-weight:800;letter-spacing:3px;color:var(--charcoal);text-transform:uppercase}
</style>
</head>
<body>
<main class="sheet">

  <section class="card card--back" aria-label="Card back">
    <div class="back-brand">
      <span class="back-brand__mark"></span>
      <span class="back-brand__name">Q7R Services</span>
    </div>
  </section>

  <section class="card card--front" aria-label="Card front">
    <svg class="card__art" viewBox="0 0 880 503" width="880" height="503" aria-hidden="true">
      <rect x="30" y="22" width="826" height="392" fill="var(--paper)"/>
      <polygon points="0,450 880,450 880,503 0,503" fill="var(--paper)"/>
      <polygon points="0,414 30,414 30,450 0,450" fill="var(--charcoal)"/>
      <polygon points="120,400 320,400 380,440 640,440 610,474 360,474 300,432 100,432" fill="var(--red)"/>
      <polygon points="650,440 880,440 880,452 660,452" fill="var(--charcoal)"/>
    </svg>

    <div class="contact">
      <h1 class="contact__title">Q7R Services</h1>
      <div class="contact__rule"></div>
      <p class="contact__motto">Design - Document<br>Develop - Deliver</p>
      <ul class="contact__list">
        <li class="contact__item">
          <span class="icon"><svg width="16" height="16" viewBox="0 0 16 16"><polygon points="1,7 15,1 10,15 8,9" fill="var(--white)"/></svg></span>
          info@Q7RServices.example
        </li>
        <li class="contact__item">
          <span class="icon"><svg width="16" height="16" viewBox="0 0 16 16"><path d="M4 1l3 3-2 2c1 2 3 4 5 5l2-2 3 3-2 3C7 15 1 9 1 4z" fill="var(--white)"/></svg></span>
          (+61) 400512836
        </li>
        <li class="contact__item">
          <span class="icon"><svg width="16" height="16" viewBox="0 0 16 16" fill="none" stroke="var(--white)" stroke-width="1.5"><circle cx="8" cy="8" r="6.5"/><ellipse cx="8" cy="8" rx="2.8" ry="6.5"/><line x1="1.5" y1="8" x2="14.5" y2="8"/></svg></span>
          Q7RServices.example
        </li>
      </ul>
    </div>

    <div class="divider"></div>

    <div class="front-brand">
      <span class="front-brand__mark"></span>
      <span class="front-brand__name">Q7R Services</span>
    </div>
  </section>

</main>
</body>
</html>
```